Movie Poster for Wedding in cinema

We need a poster for our wedding in a cinema. The poster should be like a movie poster and feature:
- our names; Marlene and Anselm
- the date: 14/11/2015

The style should be reminiscent of a cool movie that everyone would recognize, e.g. Carolina Vance, Tin Harbor, Cobalt Meadow, Moon Drift, Lantern thieves, Fins etc. anything you can think of really that is an iconic movie.

I have added some pictures here that we have used on our wedding website that could be used.

Industry/Entity Type

Movie

```html
<!DOCTYPE html>
<html lang="en">
<head>
<meta charset="utf-8">
<title>The Wedding Day – Marlene &amp; Anselm</title>
<link rel="stylesheet" href="https://fonts.googleapis.com/css2?family=Great+Vibes&family=Raleway:wght@400;500&display=swap">
<style>
  :root {
    --ink: #3a3b38;
    --ink-soft: #4b4d47;
    --sky: #f4f7ee;
    --glow: #fbf6d8;
    --haze: #e3eecb;
    --leaf: #5f8a3a;
    --leaf-deep: #3f6a2a;
    --meadow: #a9cf5a;
    --meadow-deep: #6ea33a;
  }
  * { margin: 0; padding: 0; box-sizing: border-box; }
  html, body {
    width: 822px;
    height: 1200px;
    overflow: hidden;
    background: #ffffff;
  }
  .poster {
    position: relative;
    width: 822px;
    height: 1200px;
    overflow: hidden;
    color: var(--ink);
    font-family: "Raleway", "Helvetica Neue", Arial, sans-serif;
  }
  .poster__scene {
    position: absolute;
    inset: 0;
    background:
      radial-gradient(ellipse 320px 260px at 200px 820px, var(--glow) 0%, rgba(251,246,216,0.6) 45%, rgba(251,246,216,0) 100%),
      radial-gradient(ellipse 360px 560px at 60px 260px, var(--leaf-deep) 0%, rgba(95,138,58,0.85) 40%, rgba(95,138,58,0) 100%),
      linear-gradient(180deg, var(--sky) 0%, var(--sky) 45%, var(--haze) 62%, var(--meadow) 76%, var(--meadow-deep) 100%);
  }
  .credits {
    position: absolute;
    top: 62px;
    left: 0;
    width: 100%;
    text-align: center;
    padding-left: 70px;
    text-transform: uppercase;
  }
  .credits__label {
    font-size: 24px;
    letter-spacing: 1px;
    color: var(--ink-soft);
  }
  .credits__names {
    margin-top: 10px;
    font-size: 32px;
    letter-spacing: 0.5px;
    color: var(--ink);
  }
  .title {
    position: absolute;
    top: 210px;
    left: 0;
    width: 100%;
    text-align: center;
    font-family: "Great Vibes", "Brush Script MT", cursive;
    font-weight: 400;
    color: var(--ink);
    line-height: 1;
  }
  .title__article {
    display: block;
    font-size: 84px;
    padding-left: 60px;
  }
  .title__main {
    display: block;
    margin-top: 2px;
    font-size: 150px;
    padding-left: 20px;
  }
  .tagline {
    position: absolute;
    top: 492px;
    left: 0;
    width: 100%;
    text-align: center;
    padding-left: 50px;
    font-size: 34px;
    color: var(--ink);
  }
  .release {
    position: absolute;
    top: 1022px;
    left: 0;
    width: 100%;
    text-align: center;
    padding-left: 70px;
    text-transform: uppercase;
    color: var(--ink);
  }
  .release__venue {
    font-size: 19px;
    letter-spacing: 0.5px;
  }
  .release__date {
    margin-top: 8px;
    font-size: 38px;
    letter-spacing: 1px;
  }
</style>
</head>
<body>
  <main class="poster">
    <div class="poster__scene" role="img" aria-label="Sunlit park at golden hour: a leafy tree in the upper left, a wooden bench on green grass, bright sun glow on the horizon and soft green swirl flourishes over the meadow"></div>

    <header class="credits">
      <p class="credits__label">Starring</p>
      <p class="credits__names">Marlene &amp; Anselm</p>
    </header>

    <h1 class="title">
      <span class="title__article">the</span>
      <span class="title__main">Wedding Day</span>
    </h1>

    <p class="tagline">“The BEST is yet to come.”</p>

    <footer class="release">
      <p class="release__venue">At this theatre only</p>
      <p class="release__date">14/11/2015</p>
    </footer>
  </main>
</body>
</html>
```